North American Image Consultant needs a process design and a method design

I am an Image/style consultant who works with business professionals in the Toronto area. My product name is called " R.E.S.K.A." I help people understand how your " Position, Industry, Volume, effects their Outcome and Time. I help people create a professional appearance in a business casual/digital world, from head to toe. I work with them through all 4 seasons, to achieve consistency and confidence to help them look and feel amazing, inside and out.. easily and effortlessly. My main colour is aqua blue, I don't want any neon or primary colours. I would like it to appeal to both men and women ( but mostly women)
The final design should be an easy to follow path to success with an understanding of what R.E.S.K.A will do for them.

Target Market(s)

mid level executive business professionals 38-58 yrs old they want to look and feel amazing inside and out. They want to up their game, get the promotion, nail the interview , and feel they're relevant and taken seriously in a leadership way.

Font styles to use
Serif

Colors
b7a5cd
886aae
85cae6
33a6d7
33b8a4
f04a50
00a990
e34297
85acd3

Requirements
Must have
• A classy, casual feel. A positive feel good feeling
Nice to have
• A 3 colour balance ( Not black based)
Should not have
• Too many squares
too many squiggly lines.
Not too masculine/feminine
too childish/youthful
Not office focused or bank focused

```html
<!DOCTYPE html>
<html lang="en">
<head>
<meta charset="utf-8">
<title>R.E.S.K.A – Maintaining a Professional Appearance in a Digital World</title>
<link rel="stylesheet" href="https://fonts.googleapis.com/css2?family=Quicksand:wght@600;700&family=Arimo:wght@400;700&display=swap">
<style>
  :root {
    --backdrop: #bcbfcb;
    --paper: #f2f8fb;
    --blue: #33a6d7;
    --blue-halo: #cdeaf6;
    --teal: #33b8a4;
    --teal-halo: #c9eee8;
    --purple: #886aae;
    --purple-halo: #e6ddf0;
    --white: #ffffff;
    --shadow: rgba(60, 80, 110, 0.18);
  }
  * { box-sizing: border-box; margin: 0; padding: 0; }
  html, body { width: 1200px; height: 1200px; overflow: hidden; background: var(--backdrop); }
  .poster {
    position: absolute; left: 212px; top: 50px;
    width: 776px; height: 1100px;
    background: var(--paper);
    box-shadow: 0 4px 14px rgba(0,0,0,0.12);
    overflow: hidden;
  }
  .poster-header {
    position: absolute; left: 0; top: 0; width: 100%; height: 238px;
    background: linear-gradient(90deg, var(--blue) 0%, #5e95cf 50%, var(--purple) 100%);
    color: var(--white); text-align: center;
    font-family: "Quicksand", sans-serif; font-weight: 700;
  }
  .poster-title { padding-top: 28px; font-size: 76px; letter-spacing: 3px; line-height: 1; }
  .poster-subtitle { margin-top: 24px; font-size: 31px; line-height: 46px; }
  .poster-footer { position: absolute; left: 0; bottom: 0; width: 100%; height: 27px; background: var(--blue); }

  .step { position: absolute; left: 0; width: 100%; height: 113px; }
  .step-halo { position: absolute; left: 190px; top: 4px; width: 470px; height: 105px; border-radius: 53px; }
  .step-band { position: absolute; left: 200px; top: 18px; width: 430px; height: 77px; border-radius: 39px; }
  .step-card {
    position: absolute; left: 108px; top: 0; width: 240px; height: 113px;
    border-radius: 57px; background: var(--white);
    box-shadow: 2px 3px 8px var(--shadow);
  }
  .step-letter {
    position: absolute; left: 235px; top: 13px; width: 87px; height: 87px;
    border-radius: 50%; border: 4px solid var(--white);
    box-shadow: -2px 2px 6px var(--shadow);
    color: var(--white); font-family: "Quicksand", sans-serif; font-weight: 700;
    font-size: 52px; line-height: 79px; text-align: center;
  }
  .step-icon { position: absolute; left: 138px; top: 22px; width: 80px; height: 70px; }
  .step-icon-placeholder { border-radius: 12px; opacity: 0.35; }
  .step-text { position: absolute; left: 366px; top: 28px; color: var(--white); font-family: "Arimo", sans-serif; }
  .step-heading { font-size: 21px; font-weight: 700; letter-spacing: 0.3px; line-height: 24px; }
  .step-body { font-size: 16.5px; line-height: 21px; }
  .step-text.single { top: 34px; }

  .is-blue .step-halo { background: var(--blue-halo); }
  .is-blue .step-band, .is-blue .step-letter { background: var(--blue); }
  .is-teal .step-halo { background: var(--teal-halo); }
  .is-teal .step-band, .is-teal .step-letter { background: var(--teal); }
  .is-purple .step-halo { background: var(--purple-halo); }
  .is-purple .step-band, .is-purple .step-letter { background: var(--purple); }
</style>
</head>
<body>
<main class="poster">
  <header class="poster-header">
    <h1 class="poster-title">R.E.S.K.A</h1>
    <p class="poster-subtitle">Maintaining a Professional Appearance<br>in a Digital World</p>
  </header>

  <section class="step is-blue" style="top:293px">
    <div class="step-halo"></div><div class="step-band"></div><div class="step-card"></div>
    <svg class="step-icon" viewBox="0 0 80 70" aria-label="Crown icon">
      <g fill="var(--blue)">
        <path d="M8 24 L22 40 L40 14 L58 40 L72 24 L66 52 L14 52 Z"/>
        <circle cx="8" cy="22" r="4"/><circle cx="40" cy="11" r="4"/><circle cx="72" cy="22" r="4"/>
        <rect x="14" y="56" width="52" height="6" rx="2"/>
      </g>
    </svg>
    <div class="step-letter">P</div>
    <div class="step-text">
      <h2 class="step-heading">POSITION</h2>
      <p class="step-body">Recognizing your level<br>of authority</p>
    </div>
  </section>

  <section class="step is-teal" style="top:446px">
    <div class="step-halo"></div><div class="step-band"></div><div class="step-card"></div>
    <div class="step-icon step-icon-placeholder" role="img" aria-label="Office building with a group of people" style="background:var(--teal)"></div>
    <div class="step-letter">I</div>
    <div class="step-text single">
      <h2 class="step-heading">INDUSTRY</h2>
      <p class="step-body">How it influences your message</p>
    </div>
  </section>

  <section class="step is-purple" style="top:600px">
    <div class="step-halo"></div><div class="step-band"></div><div class="step-card"></div>
    <svg class="step-icon" viewBox="0 0 80 70" aria-label="Lightning bolt icon">
      <path d="M46 2 L26 38 L40 38 L32 68 L56 26 L42 26 Z" fill="var(--purple)"/>
    </svg>
    <div class="step-letter">V</div>
    <div class="step-text">
      <h2 class="step-heading">VOLUME</h2>
      <p class="step-body">The ‘Sound’ of your presence<br>when you walk into a room</p>
    </div>
  </section>

  <section class="step is-teal" style="top:753px">
    <div class="step-halo"></div><div class="step-band"></div><div class="step-card"></div>
    <div class="step-icon step-icon-placeholder" role="img" aria-label="Hand raising a trophy" style="background:var(--teal)"></div>
    <div class="step-letter">O</div>
    <div class="step-text">
      <h2 class="step-heading">OUTCOME</h2>
      <p class="step-body">Achieve consistency<br>in your apearance</p>
    </div>
  </section>

  <section class="step is-blue" style="top:906px">
    <div class="step-halo"></div><div class="step-band"></div><div class="step-card"></div>
    <svg class="step-icon" viewBox="0 0 80 70" aria-label="Clock icon">
      <g fill="none" stroke="var(--blue)" stroke-width="4" stroke-linecap="round">
        <circle cx="40" cy="35" r="26"/>
        <path d="M40 20 V35 L30 44"/>
      </g>
    </svg>
    <div class="step-letter">T</div>
    <div class="step-text">
      <h2 class="step-heading">TIME</h2>
      <p class="step-body">Create your look<br>quickly and efficiently</p>
    </div>
  </section>

  <footer class="poster-footer"></footer>
</main>
</body>
</html>
```